Borealith Homepage Design

We need a home page design for Borealith. Borealith creates gear for outdoor enthusiasts who are passionate about conservation, wildlife observation, and ethical hunting.

Current Website: www.borealkit.com

Customer Avatar Canvas:
https://sheets.plantodeck.com/d/7XqRmTz4LkWp9VbNc2HsYd8JfGa3UeQo5iKtZrMn/edit#gid=90352114

Homepage Template: Attached below
https://files.plantodeck.com/folders/8kT3zQwLm5RpVx2NbYc7HdJf4GaUeWo

There is info on imagery in the homepage template. Where there isn't, appropriate stock imagery is acceptable.

Logo Design and Product Images: https://files.plantodeck.com/folders/3wR9yHnKb6TmQz4LpXv2CdFg8JsAeUo

```html
<!DOCTYPE html>
<html lang="en">
<head>
<meta charset="utf-8">
<title>Borealith — Home</title>
<link href="https://fonts.googleapis.com/css2?family=Exo+2:wght@600;700&family=Poppins:wght@400;500;600&family=Tinos:wght@700&display=swap" rel="stylesheet">
<style>
:root{
  --ink:#1f1f1f;
  --dark:#3a3a3a;
  --darker:#2f2f2f;
  --panel:#333333;
  --white:#ffffff;
  --muted:#555555;
  --grey-mark:#9a9a9a;
  --forest-a:#3d4a2a;
  --forest-b:#6b7a45;
}
*{margin:0;padding:0;box-sizing:border-box}
html,body{width:1200px;height:4800px;overflow:hidden}
body{position:relative;font-family:'Poppins',sans-serif;color:var(--ink);background:var(--white)}
.abs{position:absolute}
.display{font-family:'Exo 2',sans-serif;font-weight:700;text-transform:uppercase;text-align:center;letter-spacing:.5px}
.btn{position:absolute;display:flex;align-items:center;justify-content:center;font-size:14px;font-weight:500;text-transform:uppercase;text-align:center}
.btn-dark{background:var(--darker);color:var(--white);border:2px solid var(--white)}
.btn-dark.flat{border:none;background:var(--dark)}
.btn-light{background:var(--white);color:var(--ink);border:2px solid var(--dark)}
.btn-ghost{background:transparent;color:var(--white);border:2px solid var(--white)}
.brand{font-family:'Poppins',sans-serif;font-weight:600;display:flex;align-items:center;gap:10px}
.brand .sq{display:inline-block;background:currentColor}

/* header */
.site-header{top:0;left:0;width:1200px;height:127px;background:var(--white)}
.header-logo{top:0;left:88px;width:204px;height:164px;background:var(--white);justify-content:center;font-size:26px;color:var(--ink);z-index:3}
.header-logo .sq{width:18px;height:18px}
.nav{top:52px;left:405px;display:flex;gap:30px;align-items:center;font-size:13px;text-transform:uppercase}
.nav .login{display:flex;align-items:center;gap:8px}
.nav-cta{top:40px;left:708px;width:408px;height:46px;font-size:12px;background:var(--white);color:var(--ink);border:1.5px solid var(--dark)}

/* hero */
.hero{top:127px;left:0;width:1200px;height:713px;background:linear-gradient(160deg,#2f3a20 0%,var(--forest-b) 45%,#4a5530 70%,#2c3520 100%)}
.hero::after{content:"";position:absolute;inset:0;background:rgba(0,0,0,.25)}
.hero-title{top:330px;left:0;width:1200px;color:var(--white);font-size:40px;line-height:52px;z-index:2}
.hero-sub{top:540px;left:0;width:1200px;color:var(--white);font-size:39px;line-height:44px;z-index:2}

/* brand strip */
.brand-strip{top:840px;left:0;width:1200px;height:300px;display:flex;justify-content:space-around;align-items:center;padding:0 70px}
.brand-strip .brand{color:var(--grey-mark);font-size:28px}
.brand-strip .sq{width:16px;height:16px}

/* video */
.video-section{top:1140px;left:0;width:1200px;height:760px;background:var(--dark)}
.video-frame{top:1317px;left:106px;width:988px;height:336px;background:linear-gradient(120deg,#5e5a3a,#8a7f4f 40%,#6d6a42 70%,#4a4a2e)}
.play{top:1450px;left:568px}

/* how it works */
.section-mark{justify-content:center;width:100%;font-size:34px}
.section-mark .sq{width:20px;height:20px}
.how-title{top:2128px;left:449px;width:302px;text-align:center;font-family:'Poppins',sans-serif;font-weight:600;font-size:44px;border-top:3px solid var(--ink);border-bottom:3px solid var(--ink);line-height:54px}
.how-sub{top:2196px;left:0;width:1200px;text-align:center;font-size:28px;line-height:36px;font-weight:500}
.timeline{top:2232px;left:138px;height:770px;border-left:3px dotted var(--ink)}
.step-num{width:90px;height:90px;border-radius:50%;border:3px solid var(--ink);background:var(--white);display:flex;align-items:center;justify-content:center}
.step-num span{width:74px;height:74px;border-radius:50%;background:var(--dark);color:var(--white);font-family:'Tinos',serif;font-size:38px;font-weight:700;display:flex;align-items:center;justify-content:center}
.step{left:220px;width:870px}
.step h3{font-size:20px;font-weight:600;line-height:25px;margin-bottom:12px}
.step p{font-size:14px;line-height:19px;color:var(--muted)}

/* who it's for */
.who{top:3055px;left:0;width:1200px;height:980px;background:var(--dark);color:var(--white)}
.who-title{top:3295px;left:449px;width:302px;text-align:center;font-weight:600;font-size:44px;line-height:54px;border-top:3px solid var(--white);border-bottom:3px solid var(--white);color:var(--white)}
.persona-badge{width:144px;height:144px;border-radius:50%;background:var(--white);color:var(--ink);display:flex;align-items:center;justify-content:center;font-weight:600;font-size:18px}
.persona-text{width:200px;font-size:14px;line-height:25px;text-align:center;color:var(--white)}

/* cta */
.cta-title{top:4135px;left:0;width:1200px;font-size:39px;line-height:44px;color:var(--ink)}

/* footer */
.footer{top:4435px;left:0;width:1200px;height:300px;background:var(--dark);color:var(--white)}
.footer-logo{top:4540px;left:160px;font-size:36px;color:var(--white)}
.footer-logo .sq{width:20px;height:20px}
.footer h4{font-size:14px;font-weight:600;text-transform:uppercase}
.footer-links{font-size:14px;line-height:26px}
.contact-item{display:flex;align-items:center;gap:16px;font-size:14px;line-height:18px}
.icon-dot{width:30px;height:30px;border-radius:50%;background:var(--white);display:flex;align-items:center;justify-content:center;flex:none}
.bottom-bar{top:4735px;left:0;width:1200px;height:65px;background:var(--panel);color:var(--white);font-size:14px}
.social{display:flex;gap:10px}
.social span{width:34px;height:34px;border-radius:50%;border:2px solid var(--white);display:block}
</style>
</head>
<body>

<header class="site-header abs">
  <div class="header-logo abs brand"><span class="sq"></span>Borealith</div>
  <nav class="nav abs">
    <span>Features</span><span>About Us</span>
    <span class="login"><svg width="28" height="28" viewBox="0 0 28 28"><circle cx="14" cy="14" r="12.5" fill="none" stroke="#1f1f1f" stroke-width="2"/><circle cx="14" cy="11" r="4" fill="#1f1f1f"/><path d="M6.5 22c2-4 13-4 15 0" fill="#1f1f1f"/></svg>Login</span>
  </nav>
  <div class="btn nav-cta abs">Unlock the power of optics and preserve the wild</div>
</header>

<section class="hero abs" role="img" aria-label="Hunter crouching in green brush, wearing a binocular harness"></section>
<h1 class="display hero-title abs">Explore the Wild West: Embrace Conservation<br>Hunt Ethically and Protect Public Lands<br>With Borealith Gear</h1>
<h2 class="display hero-sub abs">Elevate your outdoor adventures<br>while supporting conservation efforts</h2>
<div class="btn btn-dark" style="top:677px;left:114px;width:472px;height:78px;z-index:2">Order your Borealith bino harness today!</div>
<div class="btn btn-light" style="top:677px;left:615px;width:469px;height:78px;z-index:2;border-color:#fff">Unlock the power of optics and preserve the wild</div>

<section class="brand-strip abs">
  <div class="brand"><span class="sq"></span>Borealith</div>
  <div class="brand"><span class="sq"></span>Borealith</div>
  <div class="brand"><span class="sq"></span>Borealith</div>
  <div class="brand"><span class="sq"></span>Borealith</div>
  <div class="brand"><span class="sq"></span>Borealith</div>
</section>

<section class="video-section abs"></section>
<div class="video-frame abs" role="img" aria-label="Video still of a hunter in camouflage sitting in tall grass beside antlers"></div>
<svg class="play abs" width="64" height="64" viewBox="0 0 64 64"><circle cx="32" cy="32" r="28" fill="none" stroke="#fff" stroke-width="4"/><path d="M25 19 L46 32 L25 45 Z" fill="#fff"/></svg>
<div class="btn btn-ghost" style="top:1742px;left:380px;width:474px;height:76px">Order your Borealith bino harness today!</div>

<div class="abs brand section-mark" style="top:2020px;left:0;color:var(--ink)"><span class="sq"></span>Borealith</div>
<h2 class="how-title abs">How It Works</h2>
<p class="how-sub abs">Introducing the Borealith Bino Harness<br>The Ultimate Companion for Your Optics</p>
<div class="timeline abs"></div>

<div class="step-num abs" style="top:2348px;left:94px"><span>1</span></div>
<div class="step abs" style="top:2360px">
  <h3>Experience unparalleled convenience and comfort during your outdoor excursions with the Borealith Bino Harness</h3>
  <p>Designed specifically for the modern conservationist and avid hunter, this innovative harness combines functionality, durability, and style to enhance your wildlife observation and hunting experiences.</p>
</div>
<div class="step-num abs" style="top:2498px;left:94px"><span>2</span></div>
<div class="step abs" style="top:2505px">
  <h3>Unmatched Optics Protection:</h3>
  <p>Our Bino Harness features a secure and adjustable harness system that keeps your binoculars safe and within easy reach at all times. No more fumbling around or worrying about accidentally dropping your expensive optics. With the Borealith Bino Harness, your binoculars are securely strapped to your chest, offering quick and hassle-free access whenever you need them</p>
</div>
<div class="step-num abs" style="top:2648px;left:94px"><span>3</span></div>
<div class="step abs" style="top:2652px">
  <h3>Thoughtful Design for Easy Access:</h3>
  <p>We've incorporated thoughtful design elements into the Borealith Bino Harness to enhance your outdoor adventures. The quick-release buckles allow for swift and effortless removal of the harness, granting you unhindered mobility when necessary. The adjustable straps ensure a personalized fit for individuals of all body types, providing a secure and snug grip on your binoculars.</p>
</div>
<div class="step-num abs" style="top:2798px;left:94px"><span>4</span></div>
<div class="step abs" style="top:2810px">
  <h3>Embrace Conservation:</h3>
  <p>By choosing the Borealith Bino Harness, you're not only investing in a premium gear accessory but also supporting the conservation of public lands and wildlife. We are dedicated to promoting sustainable hunting and ethical practices, and a portion of the proceeds from every purchase goes towards initiatives that preserve the habitats we hold dear.</p>
</div>

<section class="who abs"></section>
<div class="abs brand section-mark" style="top:3185px;left:0;color:var(--white)"><span class="sq"></span>Borealith</div>
<h2 class="who-title abs">Who It’s For</h2>

<div class="persona-badge abs" style="top:3413px;left:118px">Borealith</div>
<div class="persona-badge abs" style="top:3413px;left:390px">Borealith</div>
<div class="persona-badge abs" style="top:3413px;left:665px">Borealith</div>
<div class="persona-badge abs" style="top:3413px;left:933px">Borealith</div>

<p class="persona-text abs" style="top:3578px;left:90px">The Borealith Bino Harness is the ideal gear accessory for outdoor enthusiasts who are passionate about conservation, wildlife observation, and ethical hunting. This product is designed for individuals who value the preservation of public lands, appreciate the beauty of the American West, and seek to engage in sustainable and responsible outdoor pursuits.</p>
<p class="persona-text abs" style="top:3578px;left:362px">This harness is perfect for avid hunters who want quick and easy access to their binoculars without compromising on comfort. It is also ideal for wildlife photographers, birdwatchers, and nature enthusiasts who rely on high-quality optics to capture stunning images or observe wildlife in their natural habitats.</p>
<p class="persona-text abs" style="top:3578px;left:637px">Additionally, the Borealith Bino Harness appeals to those who prioritize durability and reliability in their gear. Whether you're exploring rugged terrains, participating in long hikes, or embarking on extended hunting trips, this harness will securely hold your binoculars, providing peace of mind and allowing you to focus on the beauty of nature.</p>
<p class="persona-text abs" style="top:3578px;left:905px">The Borealith Bino Harness is designed for outdoor enthusiasts who embrace a conservation centered lifestyle, value ethical hunting practices, and appreciate the unique opportunities offered by the American West.</p>

<h2 class="display cta-title abs">Elevate your outdoor adventures<br>while supporting conservation efforts</h2>
<div class="btn btn-light" style="top:4265px;left:132px;width:474px;height:77px">Unlock the power of optics and preserve the wild</div>
<div class="btn btn-dark flat" style="top:4265px;left:630px;width:470px;height:77px">Order your Borealith bino harness today!</div>

<footer class="footer abs"></footer>
<div class="footer-logo abs brand"><span class="sq"></span>Borealith</div>
<h4 class="abs" style="top:4510px;left:560px;color:var(--white);font-size:14px;font-weight:600">QUICK LINKS</h4>
<div class="footer-links abs" style="top:4560px;left:565px;color:var(--white)">Features<br>About Us<br>Login</div>
<h4 class="abs" style="top:4510px;left:825px;color:var(--white);font-size:14px;font-weight:600">CONTACT</h4>
<div class="contact-item abs" style="top:4557px;left:820px;color:var(--white)">
  <span class="icon-dot"><svg width="14" height="18" viewBox="0 0 14 18"><path d="M7 0C3 0 0 3 0 7c0 5 7 11 7 11s7-6 7-11c0-4-3-7-7-7z" fill="#3a3a3a"/><circle cx="7" cy="7" r="2.5" fill="#fff"/></svg></span>
  <span>Location Name Dummy<br>address here Pin: 123456</span>
</div>
<div class="contact-item abs" style="top:4610px;left:820px;color:var(--white)">
  <span class="icon-dot"><svg width="16" height="16" viewBox="0 0 16 16"><path d="M3 1l3 3-2 2c1 2 3 4 5 5l2-2 3 3-2 3C6 14 2 10 1 3z" fill="#3a3a3a"/></svg></span>
  <span>+0 12 3456789</span>
</div>
<div class="contact-item abs" style="top:4652px;left:820px;color:var(--white)">
  <span class="icon-dot"><svg width="16" height="12" viewBox="0 0 16 12"><rect width="16" height="12" rx="1.5" fill="#3a3a3a"/><path d="M1 1l7 6 7-6" fill="none" stroke="#fff" stroke-width="1.5"/></svg></span>
  <span>hello@borealith.com</span>
</div>

<div class="bottom-bar abs">
  <span class="abs" style="top:22px;left:90px">Copyright &nbsp;@&nbsp; 2023 All rights reserved &nbsp;| Terms &amp; Policies</span>
  <div class="social abs" style="top:15px;left:948px"><span></span><span></span><span></span><span></span></div>
</div>

</body>
</html>
```